Social Media Post – Promotion Announcement for Marcus Holloway

Objective:
Create a professional and eye-catching social media post announcing the promotion of Marcus Holloway to Vice President of Sales – Foodservice. The design should be modern, clean, and aligned with Brenwick Sales & Marketing’s branding style (friendly, West Coast, professional). It should match our website:

www.brenwicksales.example

Key Requirements:

Include Marcus Holloway’s photo (we will provide a high-resolution image).
Prominently display his name: “Marcus Holloway.”
Prominently display his new title: “Vice President of Sales – Foodservice.”

A header or highlight that says something like: “Promotion Announcement” or “Congratulations!”

Design must be editable in Canva so we can reuse the template for future promotions.

Square format (1080x1080px) for Instagram/LinkedIn, but adaptable to landscape (1200x628px) if possible.

Style Guide / Preferences:

Colors: Incorporate Brenwick Sales & Marketing brand blue (#0B64C0) along with white, gray, and/or complementary tones.

Fonts: Clean, modern sans-serif. Readable even on mobile.

Layout: Balanced between photo and text.

Option 1: Circular frame for the photo at center/top, text below.

Option 2: Split design with photo on one side and text on the other.

Tone: Professional, celebratory, approachable.

Deliverables:

Canva template file (editable).

Exported PNG/JPEG preview for review.

```html
<!DOCTYPE html>
<html lang="en">
<head>
<meta charset="UTF-8">
<title>Promotion Announcement – Marcus Holloway</title>
<link rel="stylesheet" href="https://fonts.googleapis.com/css2?family=Poppins:wght@600;700;800&display=swap">
<style>
  :root {
    --brand-blue: #3953a7;
    --sky-mid: #8196cc;
    --sky-light: #ffffff;
    --accent-yellow: #fdbd13;
    --headline-white: #ffffff;
    --portrait-dark: #4a3a2e;
    --portrait-mid: #8a7a72;
    --portrait-light: #c9c2c4;
  }
  * { margin: 0; padding: 0; box-sizing: border-box; }
  html, body {
    width: 1200px;
    height: 1200px;
    overflow: hidden;
    background: var(--sky-light);
  }
  .post {
    position: relative;
    width: 1200px;
    height: 1200px;
    overflow: hidden;
    font-family: "Poppins", sans-serif;
    background: linear-gradient(180deg, var(--brand-blue) 0%, var(--brand-blue) 22%, var(--sky-mid) 55%, var(--sky-light) 88%);
  }
  .headline {
    position: absolute;
    top: 38px;
    left: 0;
    width: 100%;
    text-align: center;
    color: var(--accent-yellow);
    font-weight: 800;
    font-size: 96px;
    letter-spacing: 1px;
    line-height: 1.1;
    white-space: nowrap;
  }
  .portrait {
    position: absolute;
    left: 0;
    top: 215px;
    width: 560px;
    height: 985px;
    border-radius: 250px 250px 0 0;
    background: linear-gradient(180deg, var(--portrait-light) 0%, var(--portrait-mid) 45%, var(--portrait-dark) 100%);
  }
  .name {
    position: absolute;
    top: 290px;
    left: 580px;
    width: 590px;
    text-align: center;
    color: var(--headline-white);
    font-weight: 800;
    font-size: 100px;
    line-height: 150px;
    letter-spacing: 0;
    white-space: nowrap;
  }
  .title {
    position: absolute;
    top: 660px;
    left: 580px;
    width: 590px;
    text-align: center;
    color: var(--brand-blue);
    font-weight: 600;
    font-size: 41px;
    line-height: 1.4;
  }
  .brand-panel {
    position: absolute;
    right: 0;
    bottom: 0;
    width: 350px;
    height: 190px;
    background: var(--sky-light);
    display: flex;
    flex-direction: column;
    justify-content: center;
    align-items: center;
    color: var(--brand-blue);
    font-weight: 700;
  }
  .brand-name {
    font-size: 50px;
    line-height: 1.05;
    letter-spacing: 0.5px;
  }
  .brand-tagline {
    font-size: 20px;
    letter-spacing: 4px;
    margin-top: 6px;
  }
</style>
</head>
<body>
  <main class="post">
    <h1 class="headline">CONGRATULATIONS!</h1>
    <div class="portrait" role="img" aria-label="Portrait photo of Marcus Holloway in a brown blazer and checked shirt"></div>
    <h2 class="name">MARCUS<br>HOLLOWAY</h2>
    <p class="title">Vice President of Sales<br>Foodservice</p>
    <div class="brand-panel" aria-label="Brenwick Sales &amp; Marketing">
      <span class="brand-name">BRENWICK</span>
      <span class="brand-tagline">Sales &amp; Marketing</span>
    </div>
  </main>
</body>
</html>
```